halbrook paving works

Needs to have phone number 0418352790 and email carlwhitby@mailnest.com.au.
ABN 27813046652
name carl whitby

For all your concreting solutions
Excavation
Exposed & colour concrete
House & shed slabs
Driveways
Landing & steps

Contact Information for Business Card

ph 0418352790
email carlwhitby@mailnest.com.au.
ABN 27813046652
name carl whitby

```html
<!DOCTYPE html>
<html lang="en">
<head>
<meta charset="utf-8">
<title>Halbrook Paving Works – Business Card</title>
<link rel="stylesheet" href="https://fonts.googleapis.com/css2?family=Lato:wght@400;700;900&display=swap">
<style>
  :root {
    --backdrop: #e5e6e7;
    --brand-orange: #f26a22;
    --brand-grey: #686868;
    --paper: #ffffff;
    --ink-light: #ffffff;
    --bullet-grey: #6b6b6b;
  }
  * { margin: 0; padding: 0; box-sizing: border-box; }
  html, body {
    width: 1200px; height: 1000px; overflow: hidden;
    background: var(--backdrop);
    font-family: "Lato", Arial, sans-serif;
  }
  .canvas { position: relative; width: 1200px; height: 1000px; }
  .card {
    position: absolute; left: 278px; width: 644px;
    display: flex; flex-direction: column;
  }
  .card--front { top: 94px; height: 394px; }
  .card--back { top: 551px; height: 393px; }
  .card__stripe { height: 30px; background: var(--brand-orange); flex: none; }
  .card__header {
    background: var(--paper); flex: none;
    display: flex; align-items: center; justify-content: center;
  }
  .card--front .card__header { height: 167px; }
  .card--back .card__header { height: 97px; }

  .brand { display: flex; align-items: center; gap: 16px; }
  .brand__square { background: var(--brand-orange); flex: none; }
  .brand__text { display: flex; flex-direction: column; align-items: center; }
  .brand__name {
    color: var(--brand-orange); font-weight: 900;
    letter-spacing: 0.5px; white-space: nowrap;
  }
  .brand__phone {
    color: var(--brand-orange); font-weight: 400; letter-spacing: 2px;
  }
  .card--front .brand__square { width: 46px; height: 46px; }
  .card--front .brand__name { font-size: 24px; }
  .card--front .brand__phone { font-size: 16px; margin-top: 4px; }
  .card--back .brand__square { width: 32px; height: 32px; }
  .card--back .brand__name { font-size: 17px; }
  .card--back .brand__phone { font-size: 12px; margin-top: 2px; }

  .card__contact {
    flex: 1; background: var(--brand-grey);
    padding: 52px 0 0 54px;
  }
  .contact__name {
    color: var(--brand-orange); font-size: 23px; font-weight: 700;
    margin-bottom: 12px;
  }
  .contact__row { display: flex; font-size: 19px; line-height: 25px; }
  .contact__label { width: 78px; color: var(--brand-orange); }
  .contact__value { color: var(--ink-light); }

  .card__services {
    flex: 1; background: var(--brand-orange);
    padding: 20px 0 0 54px; list-style: none;
  }
  .service {
    display: flex; align-items: center;
    color: var(--ink-light); font-size: 24px; height: 38px;
    white-space: nowrap;
  }
  .service__marker { width: 36px; flex: none; }
</style>
</head>
<body>
<main class="canvas">
  <section class="card card--front" aria-label="Business card front">
    <div class="card__stripe"></div>
    <header class="card__header">
      <div class="brand">
        <span class="brand__square" aria-hidden="true"></span>
        <div class="brand__text">
          <span class="brand__name">HALBROOK PAVING WORKS</span>
          <span class="brand__phone">0418352790</span>
        </div>
      </div>
    </header>
    <div class="card__contact">
      <p class="contact__name">Carl Whitby</p>
      <p class="contact__row"><span class="contact__label">Mobile</span><span class="contact__value">0418 352 790</span></p>
      <p class="contact__row"><span class="contact__label">Email</span><span class="contact__value">carlwhitby@mailnest.com.au</span></p>
      <p class="contact__row"><span class="contact__label">ABN</span><span class="contact__value">27 813 046 652</span></p>
    </div>
  </section>

  <section class="card card--back" aria-label="Business card back">
    <div class="card__stripe"></div>
    <header class="card__header">
      <div class="brand">
        <span class="brand__square" aria-hidden="true"></span>
        <div class="brand__text">
          <span class="brand__name">HALBROOK PAVING WORKS</span>
          <span class="brand__phone">0418352790</span>
        </div>
      </div>
    </header>
    <ul class="card__services">
      <li class="service"><svg class="service__marker" width="36" height="16" viewBox="0 0 36 16" aria-hidden="true"><path d="M0 1 L7 8 L0 15 Z" fill="var(--bullet-grey)"/></svg>For all your concreting solutions</li>
      <li class="service"><svg class="service__marker" width="36" height="16" viewBox="0 0 36 16" aria-hidden="true"><path d="M0 1 L7 8 L0 15 Z" fill="var(--bullet-grey)"/></svg>Excavation</li>
      <li class="service"><svg class="service__marker" width="36" height="16" viewBox="0 0 36 16" aria-hidden="true"><path d="M0 1 L7 8 L0 15 Z" fill="var(--bullet-grey)"/></svg>Exposed &amp; colour concrete</li>
      <li class="service"><svg class="service__marker" width="36" height="16" viewBox="0 0 36 16" aria-hidden="true"><path d="M0 1 L7 8 L0 15 Z" fill="var(--bullet-grey)"/></svg>House &amp; shed slabs</li>
      <li class="service"><svg class="service__marker" width="36" height="16" viewBox="0 0 36 16" aria-hidden="true"><path d="M0 1 L7 8 L0 15 Z" fill="var(--bullet-grey)"/></svg>Driveways</li>
      <li class="service"><svg class="service__marker" width="36" height="16" viewBox="0 0 36 16" aria-hidden="true"><path d="M0 1 L7 8 L0 15 Z" fill="var(--bullet-grey)"/></svg>Landing &amp; steps</li>
    </ul>
  </section>
</main>
</body>
</html>
```